MOSLEN Environmental needs an upgrade to its current business cards design

We need an upgrade to our current business cards design, where the MOSLEN acronym is included, as possible and not being overloaded.
MOSLEN Environmental is an Environmental Consultancy Firm based in Sydney.
We would like to see creative designs different from the standard type of business cards (for example, rounded edges, different to standard size of common business cards.

Target Market(s)

industrial companies (oil & gas, petrochemical, mining, insolvency, finance and manufacturing), developers, architect firms, law firms.

Industry/Entity Type

Business

Contact Information for Business Card

logos (brand and acronym), if they don't appear overloaded.
name
role
name of company (MOSLEN Environmental),
address (Level 3, Suite 3C, 47-49 Dorrigan Lane, Wexmoor, NSW, 2188) landline (02 7314 2986)
mobile (staff member)
email (staff member) and
website (www.moslengreen.example).
Include: Contaminated Land, Site Remediation, Groundwater Assessment, Health and Ecological Risk Assessments, Acid Sulfate Soils, Waste Classification.

Font styles to use
Serif
Sans Serif

Requirements
Must have
• A creative design different to the standard type of business cards.
Nice to have
• Rounded edges
• Different size of business cards rather than the standard size.
Should not have
• Preferable not to use white colour background, unless it is required from a creative design proposed.
• Not an overloaded design.
• Avoid black colours

```html
<!DOCTYPE html>
<html lang="en">
<head>
<meta charset="utf-8">
<title>MOSLEN Environmental – Business Card</title>
<link rel="stylesheet" href="https://fonts.googleapis.com/css2?family=Catamaran:wght@400;500;700;800&family=Arimo:wght@700&display=swap">
<style>
  :root {
    --backdrop: #d2d2d2;
    --card-dark: #2e2e2e;
    --card-light: #ffffff;
    --green: #7dc242;
    --grey-mark: #8a8a8a;
    --grey-word: #6e6e6e;
    --ink: #1e1e1e;
    --white: #ffffff;
  }
  * { margin: 0; padding: 0; box-sizing: border-box; }
  html, body { width: 1189px; height: 1200px; overflow: hidden; }
  body {
    background: var(--backdrop);
    font-family: "Catamaran", sans-serif;
    position: relative;
  }
  .card {
    position: absolute;
    left: 194px;
    width: 808px;
    height: 460px;
  }
  .card--front { top: 112px; background: var(--card-dark); color: var(--white); }
  .card--back { top: 619px; background: var(--card-light); color: var(--ink); }

  .divider { position: absolute; width: 2px; }
  .card--front .divider { left: 414px; top: 70px; height: 332px; background: var(--white); }
  .card--back .divider { left: 455px; top: 43px; height: 368px; background: var(--grey-word); width: 2px; }

  .brand {
    position: absolute;
    left: 53px;
    top: 160px;
    width: 308px;
    text-align: center;
    color: var(--green);
    font-weight: 800;
    line-height: 1;
  }
  .brand__name { font-size: 78px; letter-spacing: 2px; display: block; }
  .brand__sub { font-size: 24px; letter-spacing: 5px; display: block; margin-top: 6px; }

  .person { position: absolute; left: 464px; top: 74px; line-height: 1.25; }
  .person__name { font-size: 25px; font-weight: 500; }
  .person__role { font-size: 21px; font-weight: 400; }
  .person__company { font-size: 23px; font-weight: 400; color: var(--green); margin-top: 4px; }

  .contacts { position: absolute; left: 465px; top: 191px; list-style: none; }
  .contacts li {
    display: flex;
    align-items: flex-start;
    font-size: 21px;
    line-height: 27px;
    margin-bottom: 5px;
  }
  .contacts .icon {
    width: 21px; height: 21px;
    background: var(--green);
    margin-right: 16px;
    margin-top: 2px;
    flex: none;
  }
  .contacts .icon svg { display: block; width: 21px; height: 21px; }
  .contacts li.address { margin-top: 4px; }

  .services {
    position: absolute;
    right: 403px;
    top: 88px;
    list-style: none;
    text-align: right;
    font-size: 20px;
    font-weight: 500;
  }
  .services li { height: 53.6px; }

  .acronym { position: absolute; left: 497px; top: 70px; list-style: none; }
  .acronym li { display: flex; align-items: center; height: 52px; }
  .acronym__letter {
    width: 58px;
    font-size: 46px;
    font-weight: 800;
    color: var(--green);
    line-height: 1;
  }
  .acronym__word {
    font-family: "Arimo", sans-serif;
    font-weight: 700;
    font-size: 19px;
    color: var(--grey-word);
  }
</style>
</head>
<body>

<section class="card card--front">
  <div class="brand">
    <span class="brand__name">MOSLEN</span>
    <span class="brand__sub">ENVIRONMENTAL</span>
  </div>
  <div class="divider"></div>
  <div class="person">
    <p class="person__name">Dorian Kell</p>
    <p class="person__role">Project Engineer</p>
    <p class="person__company">MOSLEN Environmental</p>
  </div>
  <ul class="contacts">
    <li><span class="icon"><svg viewBox="0 0 21 21"><path d="M6 4l3 3-2 2c1 2 3 4 5 5l2-2 3 3-2 2C9 17 4 12 4 6z" fill="#2e2e2e"/></svg></span>02 7314 2986</li>
    <li><span class="icon"><svg viewBox="0 0 21 21"><rect x="7" y="3" width="7" height="15" rx="1" fill="#2e2e2e"/><rect x="8.5" y="5" width="4" height="6" fill="#7dc242"/></svg></span>0417 382 605</li>
    <li><span class="icon"><svg viewBox="0 0 21 21"><rect x="4" y="6" width="13" height="9" fill="#2e2e2e"/><path d="M4 6l6.5 5L17 6" stroke="#7dc242" stroke-width="1.2" fill="none"/></svg></span>dorian@moslengreen.example</li>
    <li><span class="icon"><svg viewBox="0 0 21 21"><circle cx="10.5" cy="10.5" r="6" fill="none" stroke="#2e2e2e" stroke-width="1.4"/><ellipse cx="10.5" cy="10.5" rx="2.6" ry="6" fill="none" stroke="#2e2e2e" stroke-width="1.2"/><path d="M4.5 10.5h12" stroke="#2e2e2e" stroke-width="1.2"/></svg></span>www.moslengreen.example</li>
    <li class="address"><span class="icon"><svg viewBox="0 0 21 21"><path d="M10.5 3a4.5 4.5 0 0 0-4.5 4.5c0 3.5 4.5 9 4.5 9s4.5-5.5 4.5-9A4.5 4.5 0 0 0 10.5 3z" fill="#2e2e2e"/><circle cx="10.5" cy="7.5" r="1.6" fill="#7dc242"/></svg></span>Level 3, Suite 3C,<br>47-49 Dorrigan Lane,<br>Wexmoor, NSW, 2188</li>
  </ul>
</section>

<section class="card card--back">
  <ul class="services">
    <li>Contaminated Land</li>
    <li>Site Remediation</li>
    <li>Groundwater Assessment</li>
    <li>Health and Ecological Risk Assessments</li>
    <li>Acid Sulfate Soils</li>
    <li>Waste Classification</li>
  </ul>
  <div class="divider"></div>
  <ul class="acronym">
    <li><span class="acronym__letter">M</span><span class="acronym__word">ANAGEMENT (OF)</span></li>
    <li><span class="acronym__letter">O</span><span class="acronym__word">N-SITE</span></li>
    <li><span class="acronym__letter">S</span><span class="acronym__word">OIL</span></li>
    <li><span class="acronym__letter">L</span><span class="acronym__word">AND (AND)</span></li>
    <li><span class="acronym__letter">E</span><span class="acronym__word">COLOGICAL</span></li>
    <li><span class="acronym__letter">N</span><span class="acronym__word">EEDS</span></li>
  </ul>
</section>

</body>
</html>
```